Letterhead for a Natural Hair Run

We need a letterhead design with the logo uploaded entitled 'Coralwave Collective'. This run is a natural 5K run seeking to promote the acceptance of natural beauty in every aspect of society encompassing one's ethnic roots and its connection to a healthy lifetstyle. We would like to see designs coordinating with our logo. The design should be fun and exciting!

Industry/Entity Type

Hair

Font styles to use
Serif
Sans Serif

Requirements
Must have
• Please included this information on the letter head:
• P.O. Box K7214
• Nassau, Bahamas
• Phone: (242) 618-2097
• Email: goskyward517@mailbrisk.net

```html
<!DOCTYPE html>
<html lang="en">
<head>
<meta charset="utf-8">
<title>Coralwave Collective Letterhead</title>
<link rel="stylesheet" href="https://fonts.googleapis.com/css2?family=Josefin+Sans:wght@400&family=Arimo&display=swap">
<style>
  :root {
    --sun: #f5e35a;
    --sea: #3fbfd6;
    --paper: #ffffff;
    --ink: #1c1c1c;
    --ghost: #dadada;
    --backdrop: #ececec;
  }
  * { margin: 0; padding: 0; box-sizing: border-box; }
  html, body { width: 992px; height: 1200px; overflow: hidden; background: var(--backdrop); }
  .letterhead {
    position: relative;
    width: 992px;
    height: 1200px;
    background: var(--paper);
  }
  .edge-band {
    position: absolute;
    left: 0;
    width: 100%;
    height: 30px;
    display: flex;
  }
  .edge-band--top { top: 0; }
  .edge-band--bottom { bottom: 0; }
  .edge-band span { display: block; height: 100%; }
  .seg-sun { background: var(--sun); }
  .seg-sea { background: var(--sea); }

  .brand {
    position: absolute;
    top: 78px;
    left: 64px;
    display: flex;
    align-items: center;
    gap: 14px;
  }
  .brand__dot {
    width: 22px; height: 22px;
    border-radius: 50%;
    background: var(--sea);
  }
  .brand__name {
    font-family: "Josefin Sans", sans-serif;
    font-weight: 400;
    font-size: 34px;
    letter-spacing: 1px;
    color: var(--ink);
  }

  .contact {
    position: absolute;
    top: 70px;
    left: 620px;
    display: flex;
    gap: 22px;
    align-items: stretch;
    font-style: normal;
  }
  .contact__rule {
    width: 2px;
    background: var(--sea);
    margin-top: 30px;
  }
  .contact__lines {
    font-family: "Arimo", sans-serif;
    font-style: normal;
    font-size: 16px;
    line-height: 1.4;
    color: var(--sun);
    list-style: none;
  }

  .watermark {
    position: absolute;
    top: 565px;
    left: 0;
    width: 100%;
    text-align: center;
    font-family: "Josefin Sans", sans-serif;
    font-weight: 400;
    font-size: 54px;
    letter-spacing: 2px;
    color: var(--ghost);
  }
</style>
</head>
<body>
  <main class="letterhead">
    <div class="edge-band edge-band--top">
      <span class="seg-sun" style="width:110px"></span>
      <span class="seg-sea" style="width:120px"></span>
      <span class="seg-sun" style="width:90px"></span>
      <span class="seg-sea" style="width:60px"></span>
      <span class="seg-sun" style="width:130px"></span>
      <span class="seg-sea" style="width:240px"></span>
      <span class="seg-sun" style="width:80px"></span>
      <span class="seg-sea" style="width:162px"></span>
    </div>

    <header class="brand">
      <span class="brand__dot"></span>
      <span class="brand__name">Coralwave Collective</span>
    </header>

    <address class="contact">
      <span class="contact__rule"></span>
      <ul class="contact__lines">
        <li>P.O. Box K7214</li>
        <li>Nassau, Bahamas</li>
        <li>Phone: (242) 618-2097</li>
        <li>Email: goskyward517@mailbrisk.net</li>
      </ul>
    </address>

    <div class="watermark">Coralwave Collective</div>

    <div class="edge-band edge-band--bottom">
      <span class="seg-sun" style="width:70px"></span>
      <span class="seg-sea" style="width:300px"></span>
      <span class="seg-sun" style="width:120px"></span>
      <span class="seg-sea" style="width:60px"></span>
      <span class="seg-sun" style="width:90px"></span>
      <span class="seg-sea" style="width:60px"></span>
      <span class="seg-sun" style="width:292px"></span>
    </div>
  </main>
</body>
</html>
```